Cybersecurity Start-Up - Korvelo

We need a power-point design for a new company based in Madrid (Spain) called 'Korvelo'. We aim to provide cybersecurity services to small- medium size companies for whom security is critical but paying big money to huge companies is not affordable.

The final design should communicate several things. As technology company which provides cybersecurity, it should be seen as something modern and futuristic , combined with safety and protection.

The company name Korvelo comes from Numantia, an ancient Celtiberian settlement in Spain which is famous for its role in the Celtiberian Wars (130 BC). They fought with Rome for 20 years , while being numerical inferior. And they won several times. When a final siege ocurred after a massive deployment of Rome legions, they held their ground for more than a year without food. When the situation was not longer sustainable, they decided to commit suicide rather than become slaves.

So the vision to hold the ground no matter what, should be communicated too
Updates

Need extra days to review

Requirements
Must have
• Check files attached for the logo of the company

```html
<!DOCTYPE html>
<html lang="en">
<head>
<meta charset="utf-8">
<title>Korvelo — Presentation Template</title>
<link rel="stylesheet" href="https://fonts.googleapis.com/css2?family=Julius+Sans+One&family=Roboto:wght@400;500;700&display=swap">
<style>
:root{
  --navy:#17243a;
  --orange:#ee5a24;
  --amber:#f7941d;
  --paper:#f1f1f1;
  --paper-edge:#d9d9d9;
  --ink:#2b2b2b;
  --muted:#555;
  --green:#2e8b57;
  --backdrop:#e4e1dc;
}
*{box-sizing:border-box;margin:0;padding:0}
html,body{width:1200px;height:1049px;overflow:hidden;background:var(--backdrop);font-family:"Roboto",Arial,sans-serif;color:var(--ink)}
.canvas{position:relative;width:1200px;height:1049px}
.slide{position:absolute;width:560px;height:314px;background:radial-gradient(ellipse at center,#fff 0%,var(--paper) 60%,var(--paper-edge) 100%);overflow:hidden;box-shadow:0 3px 8px rgba(0,0,0,.25)}
.col-a{left:32px}.col-b{left:608px}
.row-1{top:36px}.row-2{top:368px}.row-3{top:702px}

.slide-header{position:absolute;left:0;top:0;width:100%;height:40px}
.slide-header svg{position:absolute;inset:0}
.slide-title{position:absolute;left:30px;top:8px;font-family:"Julius Sans One",sans-serif;color:#fff;font-size:22px;letter-spacing:1px}
.site{position:absolute;right:10px;top:15px;color:#fff;font-size:7px;font-weight:700}

.slide-footer{position:absolute;left:22px;right:14px;bottom:14px;height:24px}
.brand{font-family:"Roboto",sans-serif;font-weight:700;color:var(--navy)}
.slide-footer .brand{position:absolute;left:0;bottom:2px;font-size:22px}
.slide-footer .rule{position:absolute;left:110px;right:16px;bottom:6px;height:1px;background:#9aa}
.slide-footer .arrow{position:absolute;right:0;bottom:1px}

.body{font-size:6.4px;line-height:1.4;color:var(--muted)}

/* cover */
.cover-brand{position:absolute;left:36px;top:128px;font-size:38px}
.cover-title{position:absolute;left:330px;top:86px;font-family:"Julius Sans One",sans-serif;color:#fff;font-size:21px;line-height:1.15;font-weight:700;letter-spacing:1px}
.cover-text{position:absolute;left:330px;top:148px;width:210px;color:#fff;font-size:6.4px;line-height:1.45}

/* contents */
.toc{position:absolute;left:32px;top:58px;display:grid;grid-template-columns:repeat(3,180px);grid-template-rows:repeat(4,44px)}
.toc-item{display:flex;gap:6px;align-items:flex-start}
.toc-num{width:30px;height:30px;background:var(--amber);color:#fff;font-size:18px;font-weight:500;display:flex;align-items:center;justify-content:center;flex:none}
.toc-item h4{font-size:7.5px;font-weight:700;margin-top:2px}
.toc-item p{font-size:5.8px;color:var(--muted);line-height:1.3}

/* about */
.about-photo{position:absolute;left:38px;top:62px;width:224px;height:120px;background:linear-gradient(135deg,#c9ced6,#8f97a3);box-shadow:2px 2px 6px rgba(0,0,0,.35)}
.about-text{position:absolute;left:290px;top:58px;width:250px;text-align:justify}
.about-text p+p{margin-top:6px}

/* mission */
.scene-photo{position:absolute;left:0;top:40px;width:330px;height:274px;background:linear-gradient(120deg,#f4f5f6 0%,#d9dde2 55%,#9da6b2 100%)}
.step{position:absolute;width:40px;height:40px;border-radius:50%;color:#fff;font-size:20px;font-weight:700;display:flex;align-items:center;justify-content:center;border:3px solid #fff;box-shadow:0 1px 4px rgba(0,0,0,.3)}
.step-1{left:210px;top:94px;background:var(--orange)}
.step-2{left:235px;top:158px;background:var(--amber)}
.step-3{left:265px;top:222px;background:var(--navy)}
.step-text{position:absolute;right:28px;width:196px;text-align:right}

/* mission & vision */
.pillar{position:absolute;top:70px;width:220px;height:200px}
.pillar-icon{position:absolute;left:0;width:52px;height:52px;border-radius:50%;background:var(--orange)}
.pillar h3{position:absolute;left:60px;font-size:18px;font-weight:700;color:#111}
.pillar .lead{position:absolute;left:60px;width:165px;font-weight:700;color:#111}
.pillar .more{position:absolute;left:60px;width:165px}

/* team */
.team{position:absolute;left:22px;top:60px;display:flex;gap:14px}
.member{width:94px;text-align:center}
.portrait{width:84px;height:84px;margin:0 auto;border-radius:50%;border:4px solid var(--orange);background:linear-gradient(160deg,#e6e8ea,#b4bac2);box-shadow:0 0 0 2px #fff inset}
.member h5{margin-top:8px;color:var(--orange);font-size:9px;font-weight:700}
.member .role{color:var(--green);font-size:6px}
.member .body{margin-top:3px;font-size:5.8px}
</style>
</head>
<body>
<div class="canvas">

  <!-- Cover -->
  <section class="slide col-a row-1">
    <svg width="560" height="314" viewBox="0 0 560 314" aria-hidden="true" style="position:absolute;inset:0">
      <path d="M300 0 Q270 170 175 314 L560 314 L560 0 Z" fill="var(--orange)"/>
      <path d="M290 0 Q258 170 160 314" fill="none" stroke="var(--amber)" stroke-width="4"/>
    </svg>
    <div class="brand cover-brand">Korvelo</div>
    <h1 class="cover-title">PRESENTATION<br>TEMPLETE</h1>
    <p class="cover-text">Lorem Ipsum is simply dummy text of the printing and typesetting industry. Lorem Ipsum has been the industry's standard dummy text ever since the 1500s, when an unknown printer took a galley of type and scrambled it to make a type specimen book. It has survived not only five centuries, but also the leap into electronic typesetting, remaining essentially unchanged. It was popularised in the 1960s with the release of transfer sheets containing Lorem Ipsum passages, and more recently with desktop publishing software including versions of Lorem Ipsum.</p>
  </section>

  <!-- Contents -->
  <section class="slide col-b row-1">
    <header class="slide-header">
      <svg width="560" height="40" viewBox="0 0 560 40" aria-hidden="true"><rect width="560" height="40" fill="var(--navy)"/><path d="M380 0 H560 V40 H395 Z" fill="var(--orange)"/></svg>
      <h2 class="slide-title">Table of Content</h2>
      <span class="site">www.KorveloSecure.com</span>
    </header>
    <div class="toc">
      <div class="toc-item"><div class="toc-num">01</div><div><h4>Your Title Here</h4><p>Lorem ipsum dolor sit amet,<br>consectetur adipiscing elit.</p></div></div>
      <div class="toc-item"><div class="toc-num">05</div><div><h4>Your Title Here</h4><p>Lorem ipsum dolor sit amet,<br>consectetur adipiscing elit.</p></div></div>
      <div class="toc-item"><div class="toc-num">09</div><div><h4>Your Title Here</h4><p>Lorem ipsum dolor sit amet,<br>consectetur adipiscing elit.</p></div></div>
      <div class="toc-item"><div class="toc-num">02</div><div><h4>Your Title Here</h4><p>Lorem ipsum dolor sit amet,<br>consectetur adipiscing elit.</p></div></div>
      <div class="toc-item"><div class="toc-num">06</div><div><h4>Your Title Here</h4><p>Lorem ipsum dolor sit amet,<br>consectetur adipiscing elit.</p></div></div>
      <div class="toc-item"><div class="toc-num">10</div><div><h4>Your Title Here</h4><p>Lorem ipsum dolor sit amet,<br>consectetur adipiscing elit.</p></div></div>
      <div class="toc-item"><div class="toc-num">03</div><div><h4>Your Title Here</h4><p>Lorem ipsum dolor sit amet,<br>consectetur adipiscing elit.</p></div></div>
      <div class="toc-item"><div class="toc-num">07</div><div><h4>Your Title Here</h4><p>Lorem ipsum dolor sit amet,<br>consectetur adipiscing elit.</p></div></div>
      <div class="toc-item"><div class="toc-num">11</div><div><h4>Your Title Here</h4><p>Lorem ipsum dolor sit amet,<br>consectetur adipiscing elit.</p></div></div>
      <div class="toc-item"><div class="toc-num">04</div><div><h4>Your Title Here</h4><p>Lorem ipsum dolor sit amet,<br>consectetur adipiscing elit.</p></div></div>
      <div class="toc-item"><div class="toc-num">08</div><div><h4>Your Title Here</h4><p>Lorem ipsum dolor sit amet,<br>consectetur adipiscing elit.</p></div></div>
      <div class="toc-item"><div class="toc-num">12</div><div><h4>Your Title Here</h4><p>Lorem ipsum dolor sit amet,<br>consectetur adipiscing elit.</p></div></div>
    </div>
    <footer class="slide-footer"><span class="brand">Korvelo</span><span class="rule"></span><svg class="arrow" width="12" height="10" viewBox="0 0 12 10" aria-hidden="true"><path d="M0 0 L12 5 L0 10 Z" fill="var(--orange)"/></svg></footer>
  </section>

  <!-- About -->
  <section class="slide col-a row-2">
    <header class="slide-header">
      <svg width="560" height="40" viewBox="0 0 560 40" aria-hidden="true"><rect width="560" height="40" fill="var(--navy)"/><path d="M380 0 H560 V40 H395 Z" fill="var(--orange)"/></svg>
      <h2 class="slide-title">About Us</h2>
      <span class="site">www.KorveloSecure.com</span>
    </header>
    <div class="about-photo" role="img" aria-label="Photo of a smiling business team giving thumbs up"></div>
    <div class="about-text body">
      <p>It has survived not only five centuries, but also the leap into electronic typesetting, remaining essentially unchanged. It was popularised in the 1960s with the release of transfer sheets containing Lorem Ipsum passages, and more recently with desktop publishing software including versions of Lorem Ipsum. Contrary to popular belief, Lorem Ipsum is not simply random text. It has roots in a piece of classical Latin literature from 45 BC, making it over 2000 years old. A Latin professor looked up one of the more obscure Latin words, consectetur, from a Lorem Ipsum passage, and going through the cites of the word in classical literature, discovered the undoubtable source. Lorem Ipsum comes from sections 1.10.32 and 1.10.33 of an old Latin text on the limits of good and evil, written in 45 BC. This book is a treatise on the theory of ethics, very popular during the Renaissance. The first line of Lorem Ipsum, "Lorem ipsum dolor sit amet..", comes from a line in section 1.10.32.</p>
      <p>Lorem Ipsum is simply dummy text of the printing and typesetting industry. Lorem Ipsum has been the industry's standard dummy text ever since the 1500s, when an unknown printer took a galley of type and scrambled it to make a type specimen book. It has survived not only five centuries, but also the leap into electronic typesetting, remaining essentially unchanged.</p>
    </div>
    <footer class="slide-footer"><span class="brand">Korvelo</span><span class="rule"></span><svg class="arrow" width="12" height="10" viewBox="0 0 12 10" aria-hidden="true"><path d="M0 0 L12 5 L0 10 Z" fill="var(--orange)"/></svg></footer>
  </section>

  <!-- Our mission -->
  <section class="slide col-b row-2">
    <header class="slide-header">
      <svg width="560" height="40" viewBox="0 0 560 40" aria-hidden="true"><rect width="560" height="40" fill="var(--navy)"/><path d="M380 0 H560 V40 H395 Z" fill="var(--orange)"/></svg>
      <h2 class="slide-title">Our Mission</h2>
      <span class="site">www.KorveloSecure.com</span>
    </header>
    <div class="scene-photo" role="img" aria-label="Photo of a team meeting in a bright office with a presenter at a whiteboard"></div>
    <div class="step step-1">1</div>
    <div class="step step-2">2</div>
    <div class="step step-3">3</div>
    <p class="step-text body" style="top:92px">Lorem ipsum dolor sit amet, consectetur adipiscing elit, sed do eiusmod tempor incididunt ut labore et dolore magna aliqua. Ut enim ad minim veniam, quis nostrud exercitation ullamco laboris nisi ut aliquip ex ea commodo consequat.</p>
    <p class="step-text body" style="top:160px">Lorem ipsum dolor sit amet, consectetur adipiscing elit, sed do eiusmod tempor incididunt ut labore et dolore magna aliqua. Ut enim ad minim veniam, quis nostrud exercitation ullamco laboris nisi ut aliquip ex ea commodo consequat.</p>
    <p class="step-text body" style="top:222px;width:186px">Lorem ipsum dolor sit amet, consectetur adipiscing elit, sed do eiusmod tempor incididunt ut labore et dolore magna aliqua. Ut enim ad minim veniam, quis nostrud exercitation ullamco laboris nisi ut aliquip ex ea commodo consequat.</p>
  </section>

  <!-- Mission & vision -->
  <section class="slide col-a row-3">
    <header class="slide-header">
      <svg width="560" height="40" viewBox="0 0 560 40" aria-hidden="true"><rect width="560" height="40" fill="var(--navy)"/><path d="M380 0 H560 V40 H395 Z" fill="var(--orange)"/></svg>
      <h2 class="slide-title">Title for the Slide</h2>
      <span class="site">www.KorveloSecure.com</span>
    </header>
    <div class="pillar" style="left:38px">
      <div class="pillar-icon" style="top:40px" role="img" aria-label="Icon of a head with gears and a money symbol"></div>
      <h3 style="top:40px">MISSION</h3>
      <p class="lead body" style="top:64px">Lorem ipsum dolor sit amet, consectetur adipiscing elit. Ut enim ad minim veniam, quis nostrud exercitation ullamco laboris</p>
      <p class="more body" style="top:96px">Lorem ipsum dolor sit amet, consectetur adipiscing elit. Ut enim ad minim veniam, quis nostrud exercitation ullamco laboris nisi ut aliquip ex ea commodo consequat<br><br>Lorem ipsum dolor sit amet, consectetur adipiscing elit. Ut enim ad minim veniam, quis nostrud exercitation ullamco laboris nisi ut aliquip ex ea commodo consequat..</p>
    </div>
    <div class="pillar" style="left:298px">
      <div class="pillar-icon" style="top:40px;width:40px;height:40px" role="img" aria-label="Icon of a head with a light bulb"></div>
      <h3 style="top:40px;left:48px">VISSION</h3>
      <p class="lead body" style="top:64px;left:48px">Lorem ipsum dolor sit amet, consectetur adipiscing elit. Ut enim ad minim veniam, quis nostrud exercitation ullamco laboris</p>
      <p class="more body" style="top:96px;left:48px">Lorem ipsum dolor sit amet, consectetur adipiscing elit. Ut enim ad minim veniam, quis nostrud exercitation ullamco laboris nisi ut aliquip ex ea commodo consequat<br><br>Lorem ipsum dolor sit amet, consectetur adipiscing elit. Ut enim ad minim veniam, quis nostrud exercitation ullamco laboris nisi ut aliquip ex ea commodo consequat..</p>
    </div>
    <footer class="slide-footer"><span class="brand">Korvelo</span><span class="rule"></span><svg class="arrow" width="12" height="10" viewBox="0 0 12 10" aria-hidden="true"><path d="M0 0 L12 5 L0 10 Z" fill="var(--orange)"/></svg></footer>
  </section>

  <!-- Team -->
  <section class="slide col-b row-3">
    <header class="slide-header">
      <svg width="560" height="40" viewBox="0 0 560 40" aria-hidden="true"><rect width="560" height="40" fill="var(--navy)"/><path d="M380 0 H560 V40 H395 Z" fill="var(--orange)"/></svg>
      <h2 class="slide-title">Our Team</h2>
      <span class="site">www.KorveloSecure.com</span>
    </header>
    <div class="team">
      <div class="member"><div class="portrait" role="img" aria-label="Portrait photo of a team member"></div><h5>Jonathan Deo</h5><div class="role">Manager</div><p class="body">Lorem Ipsum is simply dummy text of the printing and typesetting industry. Lorem Ipsum has been the industry's standard</p></div>
      <div class="member"><div class="portrait" role="img" aria-label="Portrait photo of a team member"></div><h5>Jonathan Deo</h5><div class="role">Manager</div><p class="body">Lorem Ipsum is simply dummy text of the printing and typesetting industry. Lorem Ipsum has been the industry's standard</p></div>
      <div class="member"><div class="portrait" role="img" aria-label="Portrait photo of a team member"></div><h5>Jonathan Deo</h5><div class="role">Manager</div><p class="body">Lorem Ipsum is simply dummy text of the printing and typesetting industry. Lorem Ipsum has been the industry's standard</p></div>
      <div class="member"><div class="portrait" role="img" aria-label="Portrait photo of a team member"></div><h5>Jonathan Deo</h5><div class="role">Manager</div><p class="body">Lorem Ipsum is simply dummy text of the printing and typesetting industry. Lorem Ipsum has been the industry's standard</p></div>
      <div class="member"><div class="portrait" role="img" aria-label="Portrait photo of a team member"></div><h5>Jonathan Deo</h5><div class="role">Manager</div><p class="body">Lorem Ipsum is simply dummy text of the printing and typesetting industry. Lorem Ipsum has been the industry's standard</p></div>
    </div>
    <footer class="slide-footer"><span class="brand">Korvelo</span><span class="rule"></span><svg class="arrow" width="12" height="10" viewBox="0 0 12 10" aria-hidden="true"><path d="M0 0 L12 5 L0 10 Z" fill="var(--orange)"/></svg></footer>
  </section>

</div>
</body>
</html>
```